Biz cards and stationary design
for Harbor Pathways
Project: Biz cards and stationary design
Biz cards and stationary design  - Consulting
Creative Brief
Professional
Tessa R Windrow
President
27816 Dovelin Court Haymarket, VA 20174
tessa.windrow@harborpathways-example.com
http://www.harborpathways-example.com

```html
<!DOCTYPE html>
<html lang="en">
<head>
<meta charset="utf-8">
<title>Harbor Pathways — Business Cards and Stationery</title>
<link href="https://fonts.googleapis.com/css2?family=Montserrat:wght@700&family=Open+Sans:wght@400;600&display=swap" rel="stylesheet">
<style>
  :root {
    --backdrop: #d8b98c;
    --paper: #ffffff;
    --brand-red: #8e1a22;
    --brand-red-dark: #6a0f16;
    --brand-gold: #e6a219;
    --gold-light: #f6cf3a;
    --ink: #3a3a3a;
    --rule: #c9c9c9;
    --label: #4a3a28;
  }
  html, body { margin: 0; padding: 0; overflow: hidden; }
  body { width: 1200px; height: 679px; background: var(--backdrop); }
  .stationery-board { display: block; width: 1200px; height: 679px; }
  .item-label { font-family: "Open Sans", sans-serif; font-size: 7px; fill: var(--label); }
  .brand-name { font-family: "Montserrat", sans-serif; font-weight: 700; fill: var(--brand-red); }
  .brand-name.on-dark { fill: #ffffff; }
  .body-text { font-family: "Open Sans", sans-serif; fill: var(--ink); }
  .form-title { font-family: "Open Sans", sans-serif; font-weight: 600; fill: var(--ink); }
  .paper { fill: var(--paper); }
  .band-red { fill: var(--brand-red); }
  .swoosh-gold { fill: none; stroke: var(--brand-gold); stroke-width: 2.5; }
  .form-line { fill: none; stroke: var(--rule); stroke-width: 0.8; }
  .brand-dot { fill: var(--brand-gold); }
  .footer-rule { stroke: var(--brand-gold); stroke-width: 0.8; }
</style>
</head>
<body>
<svg class="stationery-board" viewBox="0 0 1200 679" xmlns="http://www.w3.org/2000/svg">
  <defs>
    <linearGradient id="gold-card" x1="0" y1="0" x2="1" y2="1">
      <stop offset="0" stop-color="#f6cf3a"/>
      <stop offset="1" stop-color="#e6a219"/>
    </linearGradient>
    <linearGradient id="red-card" x1="0" y1="0" x2="1" y2="1">
      <stop offset="0" stop-color="#8e1a22"/>
      <stop offset="1" stop-color="#6a0f16"/>
    </linearGradient>
  </defs>

  <!-- Business cards -->
  <g class="business-card card-front" transform="translate(504,43)">
    <rect class="paper" width="148" height="62"/>
    <path class="band-red" d="M0 0 H148 V5 C100 12 45 2 0 9 Z"/>
    <circle class="brand-dot" cx="35.5" cy="20" r="2"/>
    <text class="brand-name" x="41.5" y="22.5" font-size="7" textLength="73">HARBOR PATHWAYS</text>
    <g class="body-text" font-size="3.2">
      <text x="8" y="36">Tessa R Windrow · President</text>
      <text x="8" y="41">27816 Dovelin Court Haymarket, VA 20174</text>
      <text x="8" y="46">tessa.windrow@harborpathways-example.com</text>
      <text x="104" y="36">T: 555-014-2290</text>
      <text x="104" y="41">www.harborpathways</text>
    </g>
  </g>
  <g class="business-card card-back" transform="translate(670,43)">
    <rect class="paper" width="148" height="62"/>
    <circle class="brand-dot" cx="25" cy="31" r="2.5"/>
    <text class="brand-name" x="31" y="34.5" font-size="9" textLength="94">HARBOR PATHWAYS</text>
  </g>
  <g class="business-card card-red" transform="translate(835,43)">
    <rect width="148" height="62" fill="url(#red-card)"/>
    <circle class="brand-dot" cx="25" cy="31" r="2.5"/>
    <text class="brand-name on-dark" x="31" y="34.5" font-size="9" textLength="94">HARBOR PATHWAYS</text>
  </g>
  <g class="business-card card-gold" transform="translate(1001,43)">
    <rect width="148" height="62" fill="url(#gold-card)"/>
    <circle fill="var(--brand-red)" cx="25" cy="31" r="2.5"/>
    <text class="brand-name" x="31" y="34.5" font-size="9" textLength="94">HARBOR PATHWAYS</text>
  </g>

  <!-- Fax cover -->
  <text class="item-label" x="206" y="150" text-anchor="middle">Fax Cover</text>
  <g class="fax-cover" transform="translate(29,156)">
    <rect class="paper" width="355" height="494"/>
    <path class="band-red" d="M0 0 H355 V18 C250 40 120 14 0 30 Z"/>
    <path class="swoosh-gold" d="M0 38 C120 20 260 50 355 26"/>
    <circle class="brand-dot" cx="201.5" cy="54" r="3.5"/>
    <text class="brand-name" x="209" y="58" font-size="12" textLength="125">HARBOR PATHWAYS</text>
    <text class="form-title" x="14" y="84" font-size="7">FAX</text>
    <g class="fax-fields body-text" font-size="4.5">
      <rect class="form-line" x="14" y="91" width="151" height="77"/>
      <line class="form-line" x1="14" y1="110" x2="165" y2="110"/>
      <line class="form-line" x1="14" y1="129" x2="165" y2="129"/>
      <line class="form-line" x1="14" y1="148" x2="165" y2="148"/>
      <line class="form-line" x1="40" y1="91" x2="40" y2="168"/>
      <line class="form-line" x1="88" y1="91" x2="88" y2="168"/>
      <line class="form-line" x1="114" y1="91" x2="114" y2="168"/>
      <text x="17" y="102">To:</text><text x="91" y="102">From:</text>
      <text x="17" y="121">Fax:</text><text x="91" y="121">Pages:</text>
      <text x="17" y="140">Phone:</text><text x="91" y="140">Date:</text>
      <text x="17" y="159">Re:</text><text x="91" y="159">CC:</text>
    </g>
    <g class="fax-options body-text" font-size="4.2">
      <rect class="form-line" x="14" y="178" width="5" height="5"/><text x="23" y="182.5">Urgent</text>
      <rect class="form-line" x="80" y="178" width="5" height="5"/><text x="89" y="182.5">For Review</text>
      <rect class="form-line" x="150" y="178" width="5" height="5"/><text x="159" y="182.5">Please Comment</text>
      <rect class="form-line" x="222" y="178" width="5" height="5"/><text x="231" y="182.5">Please Reply</text>
      <rect class="form-line" x="286" y="178" width="5" height="5"/><text x="295" y="182.5">Please Recycle</text>
    </g>
    <line class="footer-rule" x1="18" y1="466" x2="337" y2="466"/>
    <text class="body-text" x="178" y="475" font-size="4.2" text-anchor="middle">27816 Dovelin Court Haymarket, VA 20174 · tessa.windrow@harborpathways-example.com</text>
    <text class="body-text" x="178" y="482" font-size="4.2" text-anchor="middle">T: 555-014-2290 · http://www.harborpathways-example.com</text>
  </g>

  <!-- Letterhead -->
  <text class="item-label" x="579" y="150" text-anchor="middle">Letterhead</text>
  <g class="letterhead" transform="translate(403,156)">
    <rect class="paper" width="353" height="494"/>
    <path class="band-red" d="M0 0 H353 V18 C250 40 120 14 0 30 Z"/>
    <path class="swoosh-gold" d="M0 38 C120 20 260 50 353 26"/>
    <circle class="brand-dot" cx="172" cy="72" r="3.5"/>
    <text class="brand-name" x="179.5" y="76.5" font-size="13" textLength="136">HARBOR PATHWAYS</text>
    <line class="footer-rule" x1="18" y1="466" x2="335" y2="466"/>
    <text class="body-text" x="176" y="475" font-size="4.2" text-anchor="middle">27816 Dovelin Court Haymarket, VA 20174 · tessa.windrow@harborpathways-example.com</text>
    <text class="body-text" x="176" y="482" font-size="4.2" text-anchor="middle">T: 555-014-2290 · http://www.harborpathways-example.com</text>
  </g>

  <!-- Envelope front -->
  <text class="item-label" x="971" y="150" text-anchor="middle">Envelope (Front)</text>
  <g class="envelope-front" transform="translate(773,156)">
    <rect class="paper" width="396" height="185"/>
    <circle class="brand-dot" cx="19" cy="33" r="3"/>
    <text class="brand-name" x="26" y="37" font-size="10" textLength="100">HARBOR PATHWAYS</text>
    <text class="body-text" x="26" y="47" font-size="4">27816 Dovelin Court Haymarket, VA 20174</text>
    <path class="band-red" d="M0 140 C130 168 260 112 396 136 V185 H0 Z"/>
    <path class="swoosh-gold" d="M0 128 C130 156 260 100 396 124"/>
  </g>

  <!-- Envelope back option 1 -->
  <text class="item-label" x="971" y="359" text-anchor="middle">Envelope (Back) Option 1</text>
  <g class="envelope-back option-one" transform="translate(773,365)">
    <rect class="paper" width="396" height="76"/>
    <path d="M0 0 L198 52 L396 0" fill="none" stroke="var(--rule)" stroke-width="0.8"/>
    <circle class="brand-dot" cx="159" cy="22" r="2.5"/>
    <text class="brand-name" x="165.5" y="25" font-size="7" textLength="72">HARBOR PATHWAYS</text>
  </g>

  <!-- Envelope back option 2 -->
  <text class="item-label" x="971" y="452" text-anchor="middle">Envelope (Back) Option 2</text>
  <g class="envelope-back option-two" transform="translate(773,458)">
    <rect class="paper" width="396" height="192"/>
    <path class="band-red" d="M0 0 H396 V14 L198 66 L0 14 Z"/>
    <path d="M0 14 L198 66 L396 14" fill="none" stroke="var(--brand-gold)" stroke-width="1.5"/>
    <circle class="brand-dot" cx="149" cy="30" r="3"/>
    <text class="brand-name on-dark" x="156" y="34" font-size="9" textLength="94">HARBOR PATHWAYS</text>
  </g>
</svg>
</body>
</html>
```